Geschäftspapiere für Hersteller von Werkstattausrüstung
Zielgruppe
Werkstattausrüstung (Hebebühnen, Achsmessgeräte, Wuchtmaschinen etc.) Zielgruppe Kfz Werkstätte

```html
<!DOCTYPE html>
<html lang="de">
<head>
<meta charset="utf-8">
<title>Berger &amp; Lenz – Geschäftspapiere</title>
<link rel="stylesheet" href="https://fonts.googleapis.com/css2?family=Source+Sans+3:wght@300;400;700&display=swap">
<style>
:root{
  --bg:#e5e5e5;
  --paper:#ffffff;
  --green-dark:#006b4f;
  --green-light:#8dbf2a;
  --tint:#f0f5ee;
  --text:#1f1f1f;
  --sign:#dcdff0;
}
*{margin:0;padding:0;box-sizing:border-box}
html,body{width:1200px;height:1200px;overflow:hidden;background:var(--bg)}
body{position:relative;font-family:"Source Sans 3",sans-serif;color:var(--text)}
.sheet{position:absolute;top:262px;width:483px;height:683px;background:var(--paper);box-shadow:1px 2px 4px rgba(0,0,0,.18);overflow:hidden}
.sheet--blank{left:100px}
.sheet--letter{left:625px}
.brand{position:absolute;left:112px;top:30px;width:258px;height:40px;display:flex;align-items:center;justify-content:center;gap:10px}
.brand__dot{width:18px;height:18px;border-radius:50%;background:var(--green-light);flex:none}
.brand__name{font-weight:400;font-size:28px;line-height:1;color:var(--green-dark);white-space:nowrap}
.sender{position:absolute;left:54px;top:114px;font-size:4.6px;color:var(--green-light);white-space:nowrap}
.sender b{color:var(--green-dark)}
.fold{position:absolute;left:0;width:16px;height:1px}
.fold--upper{top:241px;background:var(--green-dark)}
.fold--lower{top:341px;background:var(--green-light)}
.watermark{position:absolute;left:98px;top:270px;width:284px;height:274px;border-radius:50%;background:var(--tint)}
.letter{position:absolute;left:54px;top:0;width:405px;font-size:7.4px;line-height:10.3px;font-weight:400;color:var(--text)}
.letter__date{position:absolute;top:253px;right:0;white-space:nowrap}
.letter__subject{position:absolute;top:283px;left:0;font-weight:700;white-space:nowrap}
.letter__greeting{position:absolute;top:324px;left:0}
.letter__body{position:absolute;top:345px;left:0;width:400px}
.letter__body p+p{margin-top:10.3px}
.letter__closing{position:absolute;top:478px;left:0}
.letter__signature{position:absolute;top:497px;left:0;width:100px;height:22px;background:var(--sign);border-radius:2px}
.letter__name{position:absolute;top:530px;left:0}
.footer{position:absolute;left:54px;top:638px;display:flex;align-items:flex-start;font-size:4.4px;line-height:7.2px;color:var(--green-light)}
.footer b{color:var(--green-dark)}
.footer__mark{width:34px;height:22px;display:flex;align-items:center}
.footer__mark span{width:14px;height:14px;border-radius:50%;background:var(--green-dark)}
.footer__col{border-left:.6px solid var(--green-dark);padding-left:4px;height:23px}
.footer__col--company{width:87px;margin-left:10px}
.footer__col--contact{width:82px}
.footer__col--register{width:107px}
.footer__col--bank{width:90px}
.footer__col dl{display:grid;grid-template-columns:auto 1fr;column-gap:3px}
.footer__col dt{font-weight:700;color:var(--green-dark)}
</style>
</head>
<body>

<section class="sheet sheet--blank">
  <header class="brand">
    <span class="brand__dot"></span>
    <span class="brand__name">Berger &amp; Lenz</span>
  </header>
  <div class="sender"><b>BERGER &amp; LENZ GmbH &amp; Co. KG</b> • Am Kranbogen 12 • 64390 Talheim</div>
  <div class="fold fold--upper"></div>
  <div class="fold fold--lower"></div>
  <div class="watermark"></div>
  <footer class="footer">
    <div class="footer__mark"><span></span></div>
    <div class="footer__col footer__col--company"><b>BERGER &amp; LENZ GMBH &amp; CO. KG</b><br>Am Kranbogen 12<br>64390 Talheim</div>
    <div class="footer__col footer__col--contact"><dl><dt>Telefon:</dt><dd>+49 (0) 6100 / 415 20 0</dd><dt>E-Mail:</dt><dd>info@berger-lenz.de</dd><dt>Internet:</dt><dd>www.berger-lenz.de</dd></dl></div>
    <div class="footer__col footer__col--register"><dl><dt>Registergericht:</dt><dd>Amtsgericht Musterstadt</dd><dt>Registernummer:</dt><dd>HRA 41207</dd><dt>USt-IdNr.</dt><dd>DE118406275</dd></dl></div>
    <div class="footer__col footer__col--bank"><dl><dt>Bank:</dt><dd>Muster Bank</dd><dt>IBAN:</dt><dd>DE12 3004 5607 0008 9911 12</dd><dt>BIC:</dt><dd>ABCDEFGH</dd></dl></div>
  </footer>
</section>

<section class="sheet sheet--letter">
  <header class="brand">
    <span class="brand__dot"></span>
    <span class="brand__name">Berger &amp; Lenz</span>
  </header>
  <div class="sender"><b>BERGER &amp; LENZ GmbH &amp; Co. KG</b> • Am Kranbogen 12 • 64390 Talheim</div>
  <div class="fold fold--upper"></div>
  <div class="fold fold--lower"></div>
  <div class="watermark"></div>
  <article class="letter">
    <div class="letter__date">Musterstadt, 18.04.2022</div>
    <div class="letter__subject">Ich bin eine Betreffzeile mit Blindtext. Ich bin eine Betreffzeile mit Blindtext.</div>
    <div class="letter__greeting">Sehr geehrte Damen und Herren,</div>
    <div class="letter__body">
      <p>ich bin Blindtext. Von Geburt an. Es hat lange gedauert, bis ich begriffen habe, was es bedeutet, ein blinder Text zu sein: Man macht keinen Sinn. Man wirkt hier und da aus dem Zusammenhang gerissen. Oft wird man gar nicht erst gelesen. Aber bin ich deshalb ein schlechter Text? Ich weiß, dass ich nie die Chance haben werde im Stern zu erscheinen. Aber bin ich darum weniger wichtig? Ich bin blind! Aber ich bin gerne Text. Und sollten Sie mich jetzt tatsächlich zu Ende lesen, dann habe ich etwas geschafft, was den meisten „normalen“ Texten nicht gelingt. Ich bin Blindtext.</p>
      <p>Und sollten Sie mich jetzt tatsächlich zu Ende lesen, dann habe ich etwas geschafft, was den meisten „normalen“ Texten nicht gelingt. Ich bin Blindtext. Von Geburt an. Es hat lange gedauert, bis ich begriffen habe, was es bedeutet, ein blinder Text zu sein: Man macht keinen Sinn. Man wirkt hier und da aus dem Zusammenhang gerissen. Oft wird man gar nicht erst gelesen. Aber bin ich deshalb ein schlechter Text? Ich weiß, dass ich nie die Chance haben werde im Stern zu erscheinen. Aber bin ich darum weniger wichtig? Ich bin blind! Aber ich bin gerne Text. Und sollten Sie mich jetzt tatsächlich zu Ende lesen, dann habe ich etwas geschafft, was den meisten „normalen“ Texten nicht gelingt.</p>
    </div>
    <div class="letter__closing">Mit freundlichen Grüßen</div>
    <div class="letter__signature" role="img" aria-label="Handschriftliche Unterschrift"></div>
    <div class="letter__name">Max Mustermann</div>
  </article>
  <footer class="footer">
    <div class="footer__mark"><span></span></div>
    <div class="footer__col footer__col--company"><b>BERGER &amp; LENZ GMBH &amp; CO. KG</b><br>Am Kranbogen 12<br>64390 Talheim</div>
    <div class="footer__col footer__col--contact"><dl><dt>Telefon:</dt><dd>+49 (0) 6100 / 415 20 0</dd><dt>E-Mail:</dt><dd>info@berger-lenz.de</dd><dt>Internet:</dt><dd>www.berger-lenz.de</dd></dl></div>
    <div class="footer__col footer__col--register"><dl><dt>Registergericht:</dt><dd>Amtsgericht Musterstadt</dd><dt>Registernummer:</dt><dd>HRA 41207</dd><dt>USt-IdNr.</dt><dd>DE118406275</dd></dl></div>
    <div class="footer__col footer__col--bank"><dl><dt>Bank:</dt><dd>Muster Bank</dd><dt>IBAN:</dt><dd>DE12 3004 5607 0008 9911 12</dd><dt>BIC:</dt><dd>ABCDEFGH</dd></dl></div>
  </footer>
</section>

</body>
</html>
```